CareLumen business cards

We need a business card design that we could customize as needed for employees. We will need space for Name, Title, 1-2 phone numbers and email address.

We are a Pharmacy Benefits Management (PBM) company for hospice agencies and beginning a nationwide expansion. Attached is a vector file of our logo.

Cards can be single or double sided.

```html
<!DOCTYPE html>
<html lang="en">
<head>
<meta charset="utf-8">
<title>CareLumen business cards</title>
<link rel="stylesheet" href="https://fonts.googleapis.com/css2?family=Source+Sans+3:wght@400;600&display=swap">
<style>
  :root {
    --backdrop: #e8e5e0;
    --card-black: #000000;
    --card-white: #ffffff;
    --brand-green: #7f9a5c;
    --brand-blue: #2f6789;
    --band-blue: #326a8d;
    --rule-green: #a3b57c;
    --text-white: #ffffff;
    --text-soft: #e6e6e6;
    --text-grey: #555555;
    --divider: #8a8a8a;
  }
  * { margin: 0; padding: 0; box-sizing: border-box; }
  html, body {
    width: 1056px; height: 1200px; overflow: hidden;
    background: var(--backdrop);
    font-family: "Source Sans 3", "Myriad Pro", Arial, sans-serif;
  }
  .card {
    position: absolute; left: 78px; width: 900px; height: 540px; overflow: hidden;
  }
  .card--front { top: 40px; background: var(--card-black); }
  .card--back { top: 620px; background: var(--card-white); }

  .brand {
    position: absolute; left: 0; right: 0; top: 130px;
    display: flex; align-items: center; justify-content: center; gap: 18px;
  }
  .brand__mark { width: 56px; height: 56px; border-radius: 8px; background: var(--brand-green); }
  .brand__name { font-size: 72px; font-weight: 400; color: var(--brand-green); letter-spacing: -1px; line-height: 1; }

  .identity {
    position: absolute; right: 478px; top: 288px; text-align: right; color: var(--text-white);
  }
  .identity__name { font-size: 32px; font-weight: 600; line-height: 1.05; }
  .identity__title { font-size: 24px; color: var(--brand-green); line-height: 1.2; margin-bottom: 12px; }
  .identity__address { font-size: 19px; line-height: 1.45; color: var(--text-soft); }

  .divider {
    position: absolute; left: 435px; top: 291px; width: 1px; height: 134px; background: var(--divider);
  }

  .contacts {
    position: absolute; left: 452px; top: 300px; list-style: none; color: var(--text-white);
  }
  .contacts li { display: flex; align-items: center; gap: 10px; font-size: 21px; height: 42px; }
  .contacts svg { width: 18px; height: 18px; fill: var(--text-soft); }

  .rule { position: absolute; left: 0; right: 0; top: 447px; height: 2px; background: var(--rule-green); }
  .band {
    position: absolute; left: 0; right: 0; top: 452px; bottom: 0; background: var(--band-blue);
    display: flex; align-items: center; justify-content: center;
    color: var(--text-white); font-size: 24px; letter-spacing: 4px;
  }

  .back-brand {
    position: absolute; left: 0; right: 0; top: 195px; text-align: center;
    font-size: 118px; font-weight: 400; color: var(--brand-blue); letter-spacing: -2px; line-height: 1;
  }
  .back-url {
    position: absolute; left: 0; right: 0; top: 445px; text-align: center;
    font-size: 32px; letter-spacing: 3px; color: var(--text-grey);
  }
</style>
</head>
<body>
  <section class="card card--front">
    <div class="brand">
      <span class="brand__mark"></span>
      <span class="brand__name">CareLumen</span>
    </div>

    <div class="identity">
      <p class="identity__name">Your Name</p>
      <p class="identity__title">Title</p>
      <p class="identity__address">Sreet Name, City Name<br>Zip Code-00000</p>
    </div>

    <span class="divider"></span>

    <ul class="contacts">
      <li>
        <svg viewBox="0 0 24 24" aria-hidden="true"><path d="M6.6 10.8a15 15 0 0 0 6.6 6.6l2.2-2.2c.3-.3.7-.4 1-.2 1.1.4 2.3.6 3.6.6.6 0 1 .4 1 1V20c0 .6-.4 1-1 1A17 17 0 0 1 3 4c0-.6.4-1 1-1h3.5c.6 0 1 .4 1 1 0 1.3.2 2.5.6 3.6.1.3 0 .7-.2 1l-2.3 2.2z"/></svg>
        012-345-6789
      </li>
      <li>
        <svg viewBox="0 0 24 24" aria-hidden="true"><path d="M7 3h10v5H7zM4 9h16a2 2 0 0 1 2 2v6h-4v4H6v-4H2v-6a2 2 0 0 1 2-2zm4 7v3h8v-3z"/></svg>
        012-345-6789
      </li>
      <li>
        <svg viewBox="0 0 24 24" aria-hidden="true"><path d="M2 5h20v14H2zm2 2v.5l8 5 8-5V7zm0 2.8V17h16V9.8l-8 5z"/></svg>
        info@carelumen.com
      </li>
    </ul>

    <span class="rule"></span>
    <div class="band">www.carelumen.com</div>
  </section>

  <section class="card card--back">
    <p class="back-brand">CareLumen</p>
    <p class="back-url">www.carelumen.com</p>
  </section>
</body>
</html>
```